Wine Label named: Amber Ridge

We are a wine producer, who wishes to launch a new premium wine called: Amber Ridge
Our winery is situated in a rolling hill, with slopes, where Amber Ridge exists in the property. One dates to the 15th century and the other more recent to the 18th century. Its a unique feature of the winery and we wish to create a label that represents these, but is NOT religious! Difficult task I know. Think you can pull it off? Let us see it! We start with one label, but the winner will have 5 more labels to design.

Target Market(s)

30-50 year old men

Industry/Entity Type

Wine

Colors

Designer to choose colors to be used in the design.

Requirements
Must have
• serious look and premium feel. name of the wine: Amber Ridge
Nice to have
• 2019 14% ABV
Should not have
• a religious look and feel

```html
<!DOCTYPE html>
<html lang="en">
<head>
<meta charset="utf-8">
<title>Amber Ridge – Red Wine Label</title>
<link rel="stylesheet" href="https://fonts.googleapis.com/css2?family=Josefin+Sans:wght@300;400;600&display=swap">
<style>
  :root {
    --label-black: #0d0f11;
    --cream: #f8eee0;
    --gold-text: #eed293;
    --gold-frame: #a88a55;
    --burgundy: #6e2033;
    --divider-gold: #c9a56a;
  }
  html, body {
    margin: 0;
    padding: 0;
    background: var(--label-black);
    overflow: hidden;
  }
  .label {
    position: relative;
    width: 764px;
    height: 1200px;
    background: var(--label-black);
    font-family: "Josefin Sans", sans-serif;
    color: var(--cream);
    overflow: hidden;
  }
  .brand-mark {
    position: absolute;
    top: 62px;
    left: 0;
    width: 100%;
    display: flex;
    justify-content: center;
    align-items: center;
    gap: 22px;
    font-size: 19px;
    letter-spacing: 0.08em;
  }
  .brand-mark__name {
    display: flex;
    align-items: center;
    gap: 8px;
    font-weight: 400;
  }
  .brand-mark__square {
    width: 10px;
    height: 10px;
    background: var(--cream);
  }
  .title {
    position: absolute;
    top: 165px;
    left: 0;
    width: 100%;
    text-align: center;
    margin: 0;
    font-weight: normal;
  }
  .title__main {
    display: block;
    font-weight: 600;
    font-size: 118px;
    line-height: 1;
    letter-spacing: 0.1em;
    padding-left: 0.1em;
    color: var(--cream);
  }
  .title__sub {
    display: block;
    margin-top: 22px;
    font-weight: 400;
    font-size: 68px;
    line-height: 1;
    letter-spacing: 0.1em;
    padding-left: 0.1em;
    color: var(--gold-text);
  }
  .landscape {
    position: absolute;
    left: 108px;
    top: 430px;
    width: 547px;
    height: 566px;
    border: 3px solid var(--gold-frame);
    background: linear-gradient(180deg,
      #f9eee0 0%, #f6e6cf 28%, #b9a766 36%, #8f8c4a 52%,
      #c8a456 66%, #7c7a3a 82%, #a89048 100%);
  }
  .wine-type {
    position: absolute;
    top: 1040px;
    left: 0;
    width: 100%;
    text-align: center;
    font-size: 40px;
    font-weight: 400;
    letter-spacing: 0.07em;
  }
  .info-band {
    position: absolute;
    left: 0;
    bottom: 0;
    width: 100%;
    height: 86px;
    background: var(--burgundy);
    display: flex;
    align-items: center;
    font-size: 24px;
    font-weight: 600;
    letter-spacing: 0.1em;
  }
  .info-band__item {
    text-align: center;
    padding-top: 4px;
  }
  .info-band__item--abv { width: 213px; }
  .info-band__item--origin { width: 337px; }
  .info-band__item--volume { flex: 1; }
  .info-band__divider {
    width: 4px;
    height: 42px;
    background: var(--divider-gold);
  }
</style>
</head>
<body>
  <main class="label">
    <div class="brand-mark">
      <span class="brand-mark__estd">ESTD</span>
      <span class="brand-mark__name"><span class="brand-mark__square"></span>AMBER RIDGE</span>
      <span class="brand-mark__year">2019</span>
    </div>

    <h1 class="title">
      <span class="title__main">AMBER</span>
      <span class="title__sub">RIDGE</span>
    </h1>

    <div class="landscape" role="img" aria-label="Golden evening view of rolling vineyard hills with two white farm buildings on the slopes"></div>

    <p class="wine-type">Red Wine</p>

    <footer class="info-band">
      <span class="info-band__item info-band__item--abv">14% ABV</span>
      <span class="info-band__divider"></span>
      <span class="info-band__item info-band__item--origin">MADE IN SPAIN</span>
      <span class="info-band__divider"></span>
      <span class="info-band__item info-band__item--volume">70cl</span>
    </footer>
  </main>
</body>
</html>
```